Shop Window Desgin

I have a big glass window (office), 280cm wide by 302cm high and I want designing an advert for our property management business.

Our main colours are in the proeprty management logo attached. I have also uploaded a photo of the shop front (left window), please take into consideration the door.

I want the following text items placed:

PROPERTY MANAGEMENT
HOLIDAY RENTALS
KEYHOLDING
MARKETING & RESERVATIONS
GARDEN & POOL MAINTENACE
CLEANING & LAUNDRY

```html
<!DOCTYPE html>
<html lang="en">
<head>
<meta charset="utf-8">
<title>Keystone Property Management – Shop Window Advert</title>
<link rel="stylesheet" href="https://fonts.googleapis.com/css2?family=Bebas+Neue&display=swap">
<style>
  :root {
    --backdrop: #58585a;
    --panel: #ffffff;
    --orange: #e98024;
    --navy: #0b4a78;
    --cyan: #12ace0;
    --ink: #111111;
    --sky-light: #e6f4fb;
    --sky-blue: #8fcdea;
    --grass: #b9d98a;
    --water: #7cc4e6;
    --badge-purple: #4b3560;
    --badge-blue: #1e88c8;
  }
  * { margin: 0; padding: 0; box-sizing: border-box; }
  html, body { width: 960px; height: 1200px; overflow: hidden; }
  body { background: var(--backdrop); position: relative; font-family: "Bebas Neue", "Oswald", sans-serif; }

  .window-advert {
    position: absolute; left: 46px; top: 132px;
    width: 868px; height: 936px;
    background: var(--panel); overflow: hidden;
  }

  .brand {
    position: absolute; left: 0; top: 40px; width: 100%; height: 96px;
    display: flex; align-items: center; justify-content: center; gap: 16px;
    white-space: nowrap;
  }
  .brand-dot { flex: 0 0 auto; width: 54px; height: 54px; border-radius: 50%; background: var(--orange); }
  .brand-name { color: var(--orange); font-size: 58px; line-height: 1; letter-spacing: 1px; padding-top: 6px; }

  .scene { position: absolute; left: 0; width: 100%; }
  .scene-city {
    top: 158px; height: 320px;
    background: linear-gradient(180deg, var(--sky-blue) 0%, var(--sky-light) 30%, #ffffff 55%, var(--sky-light) 80%, var(--grass) 100%);
  }
  .scene-park {
    top: 548px; height: 188px;
    background: linear-gradient(90deg, var(--water) 0%, #bfe3f0 35%, #e9f3e0 65%, #ffffff 100%);
  }

  .band {
    position: absolute; left: 0; width: 100%;
    display: flex; align-items: center; justify-content: center;
    color: #ffffff; line-height: 1; padding-top: 6px; font-weight: 400;
    white-space: nowrap;
  }
  .band-orange { top: 158px; height: 72px; background: var(--orange); font-size: 76px; }
  .band-navy { top: 478px; height: 70px; background: var(--navy); font-size: 74px; }
  .band-cyan { top: 736px; height: 68px; background: var(--cyan); font-size: 68px; }

  .service {
    position: absolute; left: 0; width: 100%; text-align: center; line-height: 1; white-space: nowrap;
  }
  .service-primary { color: var(--navy); font-size: 76px; }
  .service-secondary { color: var(--ink); font-size: 64px; }
  .holiday { top: 274px; }
  .keyholding { top: 362px; }
  .garden { top: 582px; }
  .maintenance { top: 654px; }

  .badge { position: absolute; }
  .badge-association { left: 46px; top: 848px; width: 222px; height: 52px; background: var(--badge-purple); border-radius: 4px; }
  .badge-certificate { left: 702px; top: 812px; width: 120px; height: 110px; background: var(--badge-blue); border-radius: 32px; }
</style>
</head>
<body>
  <main class="window-advert">
    <header class="brand">
      <span class="brand-dot" aria-hidden="true"></span>
      <span class="brand-name">Keystone Property Management</span>
    </header>

    <div class="scene scene-city" role="img" aria-label="Illustration of bright modern city buildings under a blue sky"></div>
    <div class="scene scene-park" role="img" aria-label="Illustration of a swimming pool beside a garden with trees"></div>

    <h1 class="band band-orange">Property Management</h1>

    <p class="service service-primary holiday">Holiday Rentals</p>
    <p class="service service-primary keyholding">Keyholding</p>

    <h2 class="band band-navy">Marketing &amp; Reservations</h2>

    <p class="service service-secondary garden">Garden &amp; Pool</p>
    <p class="service service-secondary maintenance">Maintenace</p>

    <h2 class="band band-cyan">Cleaning &amp; Laundry</h2>

    <div class="badge badge-association" role="img" aria-label="Trade association membership badge"></div>
    <div class="badge badge-certificate" role="img" aria-label="Pool and spa operator certification badge"></div>
  </main>
</body>
</html>
```